christmas poster

Gift Vouchers Promotion

Buy 3 of Any Value
Get 1 More Free

The Poster Should be very modern but with a relevance to Christmas

Target Market(s)

Affluent Clients

Font styles to use
Decorative

Colors
ec1f27

Requirements
Must have
• Modern Clean Feel but Relevant to Christmas
Nice to have
• The Offer:
• Buy 3 Gift Vouchers and Receive 1 More Fee
• MUST be Big and Bold
• Include Logo

```html
<!DOCTYPE html>
<html lang="en">
<head>
<meta charset="utf-8">
<title>Christmas Gift Voucher Poster</title>
<link rel="stylesheet" href="https://fonts.googleapis.com/css2?family=Sacramento&family=Josefin+Sans:wght@400;600&display=swap">
<style>
  :root {
    --festive-red: #ec1f27;
    --paper-white: #ffffff;
    --ink-black: #111111;
  }
  html, body {
    margin: 0;
    padding: 0;
    overflow: hidden;
    background: var(--paper-white);
  }
  .poster-canvas {
    position: relative;
    width: 1200px;
    height: 1000px;
    overflow: hidden;
    background: var(--paper-white);
  }
  .poster-backdrop {
    position: absolute;
    left: 0;
    top: 0;
  }
  .offer-line {
    position: absolute;
    left: 0;
    width: 1250px;
    margin: 0;
    text-align: center;
    font-family: "Sacramento", cursive;
    font-weight: 400;
    color: var(--ink-black);
    line-height: 1;
    white-space: nowrap;
  }
  .offer-number {
    font-family: "Josefin Sans", sans-serif;
    display: inline-block;
    margin-right: 8px;
  }
  .line-buy { top: 66px; font-size: 98px; }
  .line-gift { top: 200px; font-size: 94px; }
  .line-gift .offer-number { font-size: 112px; font-weight: 600; vertical-align: 2px; }
  .line-vouchers { top: 352px; font-size: 98px; }
  .line-receive { top: 484px; font-size: 100px; }
  .line-more { top: 626px; font-size: 100px; }
  .line-more .offer-number { font-size: 124px; font-weight: 400; vertical-align: -4px; margin-right: 22px; }
  .line-free { top: 768px; font-size: 100px; }
  .tree-exclaim {
    display: inline-block;
    vertical-align: -8px;
    margin-left: 14px;
  }
  .brand-name {
    position: absolute;
    left: 0;
    width: 1250px;
    top: 900px;
    margin: 0;
    text-align: center;
    font-family: "Sacramento", cursive;
    font-size: 46px;
    color: var(--festive-red);
    line-height: 1;
  }
</style>
</head>
<body>
  <main class="poster-canvas">
    <svg class="poster-backdrop" width="1200" height="1000" viewBox="0 0 1200 1000" aria-hidden="true">
      <rect x="265" y="10" width="690" height="978" fill="var(--festive-red)"/>
      <polygon class="christmas-tree" fill="var(--paper-white)"
        points="522,10 722,10 864,259 718,258 905,557 772,568 935,970 287,977 466,568 343,567 508,260 397,258"/>
    </svg>

    <p class="offer-line line-buy">Buy</p>
    <p class="offer-line line-gift"><span class="offer-number">3</span>Gift</p>
    <p class="offer-line line-vouchers">Vouchers</p>
    <p class="offer-line line-receive">Receive</p>
    <p class="offer-line line-more"><span class="offer-number">1</span>More</p>
    <p class="offer-line line-free">Free<svg class="tree-exclaim" width="40" height="100" viewBox="0 0 46 104" aria-label="exclamation tree">
        <polygon points="23,0 36,26 30,26 41,52 33,52 46,84 0,84 13,52 5,52 16,26 10,26" fill="var(--ink-black)"/>
        <rect x="19" y="92" width="8" height="10" fill="var(--ink-black)"/>
      </svg></p>

    <p class="brand-name">Verelle salon &amp; spa</p>
  </main>
</body>
</html>
```